Meridian Prestige Academy needs a Courses Fine Brochure

An unique business school 100% focused on the luxury market that offers programs in NY, L.A., Miami, Paris, Milan, and São Paulo, needs a comprehensive brochure with all your programs.
In two versions, to print and as a web flipping book.
Please find attached two examples of our single program brochures.
PLEASE NOTE THAT ALL UPLOADED MATERIALS ARE SAMPLES OF WHAT WE ALREADY DID, AS SOON AS I´VE CHOSEN A DESIGNER I´LL SEND THE CORRECT FILES, TEXTS AND "SUGGESTED IMAGES".
Updates

Target Market(s)

US students interested in short term programs focused on luxury.
The brochure must display 12 short term programs that will take place in 2017 in Miami, Florida.

Industry/Entity Type

Education

Contact Information for Business Card

Black sober fine finishing business card.
Name, place, phone, address, e-mail, cel.

Font styles to use
Serif
Sans Serif
Script

Requirements
Must have
• Fine finishing, as smooth touch mate lamination, and/or hotstamping, and/or located varnish.
• Easy to read. Every program has Name, brief introduction, date, time, duration, some keynote speaker picture and brief resumé (short cv). And 5 to 10 content topics. Course highlights.
Nice to have
• Luxury products and services. Sofisticated images, closeups and nice views.
• We are talking about teaching luxury for entrepreneurs mainly.
• Business owners or high level executives.
Should not have
• Less is more. Promotional look. Cheap look. Colorful blasting design.

```html
<!DOCTYPE html>
<html lang="en">
<head>
<meta charset="utf-8">
<title>Luxury Hospitality Summit – Brochure Spreads</title>
<link rel="stylesheet" href="https://fonts.googleapis.com/css2?family=Great+Vibes&family=Open+Sans:wght@400;600;700&family=Oswald:wght@300;400;500&display=swap">
<style>
:root{
  --bg:#eceaed;
  --ink:#141414;
  --gold:#d6a844;
  --gold-deep:#c9963a;
  --white:#ffffff;
  --time:#6b4a12;
  --rule:#c9cfcc;
  --label:#2b2b2b;
}
*{box-sizing:border-box;margin:0;padding:0}
html,body{width:1200px;height:1200px;overflow:hidden;background:var(--bg)}
body{position:relative;font-family:"Open Sans",sans-serif;color:var(--ink)}
.spread{position:absolute;width:778px;height:276px;overflow:hidden;box-shadow:0 8px 14px rgba(0,0,0,.18)}
.spread--one{left:209px;top:178px}
.spread--two{left:211px;top:779px}
.page-label{position:absolute;font-size:15px;color:var(--label);letter-spacing:.5px}
.abs{position:absolute}
.brand{font-family:"Open Sans",sans-serif;font-weight:600;font-size:9px;letter-spacing:.4px}
.event{font-family:"Oswald",sans-serif;font-weight:300;font-size:9px;line-height:11px}
.script{font-family:"Great Vibes",cursive}

/* spread one */
.cover-photo{left:0;top:0;width:390px;height:276px;background:linear-gradient(180deg,#e89a6f 0%,#f4b07e 40%,#b9735a 62%,#6d4a47 78%,#c7866b 100%)}
.cover .brand{left:10px;top:14px;color:var(--white)}
.cover .event{left:10px;top:40px;color:var(--white)}
.diamond{left:130px;top:76px;width:139px;height:139px;background:#2f2f2f;transform:rotate(45deg)}
.cover-date{left:100px;top:110px;width:200px;text-align:center;color:var(--white);font-family:"Oswald",sans-serif;font-size:22px}
.cover-title{left:100px;top:136px;width:200px;text-align:center;color:var(--white);font-size:24px}
.intro-col{left:390px;top:0;width:131px;height:276px;background:var(--ink);color:#e2e2e2;padding:28px 10px 0 10px;font-size:7px;line-height:12px}
.intro-col p+p{margin-top:12px}
.schedule{left:521px;top:0;width:257px;height:276px}
.schedule-photo{left:0;top:0;width:257px;height:276px;background:linear-gradient(160deg,#e7ece8 0%,#d6e3df 50%,#bcd9d6 100%)}
.schedule-tag{left:0;top:10px;width:82px;height:13px;background:var(--gold);color:var(--white);font-size:12px;line-height:13px;padding-left:16px}
.row{position:absolute;left:10px;width:165px;font-size:7px;display:flex;align-items:center}
.row .time{font-family:"Open Sans",sans-serif;font-weight:700;font-size:8.5px;color:var(--time);width:50px}
.row .time::before{content:"";display:inline-block;width:3px;height:3px;border:1px solid var(--time);border-radius:50%;margin-right:3px;vertical-align:1px}
.row::after{content:"";position:absolute;left:0;right:0;bottom:-5px;border-bottom:1px solid var(--rule)}
.sub{position:absolute;left:60px;font-size:5.5px}
.cocktail{right:8px;top:128px;text-align:right;color:var(--white);font-size:15px;line-height:17px}
.footnote{right:0;top:258px;font-size:4.5px;line-height:6px;text-align:left}

/* spread two */
.speakers-head{left:0;top:0;width:388px;height:78px;background:linear-gradient(90deg,#fff 0%,#fff 55%,#cfcfcf 100%)}
.speakers-head .brand{left:17px;top:8px;color:var(--gold-deep)}
.speakers-head .event{left:16px;top:33px;color:var(--ink)}
.speakers-title{right:24px;top:30px;font-size:27px;color:var(--ink)}
.speakers-body{left:0;top:78px;width:388px;height:198px;background:var(--gold)}
.speakers-intro{left:12px;top:14px;width:104px;color:var(--white);font-size:6.8px;line-height:12px}
.speakers-intro p+p{margin-top:12px}
.speaker{position:absolute;top:15px;width:75px;text-align:center;color:var(--white)}
.speaker-photo{width:67px;height:77px;margin:0 auto;background:linear-gradient(180deg,#5a4a3f,#2a2321)}
.speaker-name{font-family:"Oswald",sans-serif;font-size:7.5px;margin-top:3px}
.speaker-role{font-family:"Oswald",sans-serif;font-weight:300;font-size:5.5px;line-height:6.5px}
.speaker-bio{font-size:5.2px;line-height:6.5px;margin-top:5px}
.topics-col{left:388px;top:0;width:141px;height:276px;background:var(--ink);padding:20px 8px 0 8px}
.topics-title{color:var(--gold);font-size:20px;margin-bottom:12px}
.topics-col ul{list-style:none}
.topics-col li{position:relative;padding-left:8px;color:#e8e8e8;font-size:5.6px;line-height:7px;height:23.5px}
.topics-col li::before{content:"";position:absolute;left:0;top:2px;width:3px;height:3px;border-radius:50%;background:var(--gold)}
.pool-photo{left:529px;top:0;width:249px;height:276px;background:linear-gradient(180deg,#3d7fb6 0%,#8ec0d8 30%,#6c9a6e 50%,#2fb7bf 75%,#1f8c99 100%)}
.highlights{left:633px;top:178px;width:139px;height:82px;background:var(--gold);padding:7px 13px;color:var(--white)}
.highlights-title{font-size:15px;margin-bottom:6px}
.highlights p{font-size:5.6px;line-height:7px}
.highlights p+p{margin-top:5px}
</style>
</head>
<body>

<section class="spread spread--one">
  <div class="cover">
    <div class="abs cover-photo" role="img" aria-label="Sunset skyline of Miami over the bay"></div>
    <div class="abs brand">Meridian Prestige Academy</div>
    <div class="abs event">Luxury Hospitality Summit®<br>Miami, Florida - 2017</div>
    <div class="abs diamond"></div>
    <div class="abs cover-date">25/07</div>
    <div class="abs cover-title script">A new luxury hospitality?</div>
  </div>

  <div class="abs intro-col">
    <p>There are many variations of passages of Lorem Ipsum available, but the majority have suffered alteration in some form, by injected humour, or randomised words which don't look even slightly believable.</p>
    <p>If you are going to use a passage of Lorem Ipsum, you need to be sure there isn't anything embarrassing hidden in the middle of text.</p>
    <p>All the Lorem Ipsum generators on the Internet tend to repeat predefined chunks as necessary, making this the first true generator on the Internet.</p>
  </div>

  <div class="abs schedule">
    <div class="abs schedule-photo" role="img" aria-label="Faded view of a hotel poolside cabana"></div>
    <div class="abs schedule-tag script">Our Schedule</div>
    <div class="row" style="top:30px"><span class="time">09h00</span>- Official Opening</div>
    <div class="row" style="top:47px"><span class="time">09h15</span>- Luxury Distribution</div>
    <div class="sub" style="top:64px">Special Lecture about sales</div>
    <div class="row" style="top:80px"><span class="time">10h30</span>- Coffee-break</div>
    <div class="row" style="top:97px"><span class="time">10h45</span>- Grand Rivage Paris - It´s Alive!</div>
    <div class="sub" style="top:115px">Hotel Site Inspection</div>
    <div class="row" style="top:130px"><span class="time">12h00</span>- Lunch</div>
    <div class="row" style="top:146px"><span class="time">14h00</span>- Le Solstice</div>
    <div class="sub" style="top:164px">Hotel Site Inspection</div>
    <div class="row" style="top:180px"><span class="time">15h30</span>- Coffee-break</div>
    <div class="row" style="top:197px"><span class="time">15h45</span>- Meeting Compendium</div>
    <div class="sub" style="top:214px">Panel of perceptions and forecasts</div>
    <div class="row" style="top:230px"><span class="time">17h00</span>- Certificates</div>
    <svg class="abs" style="left:0;top:0" width="257" height="276" aria-hidden="true">
      <polygon points="257,59 165,142 257,235" fill="#d6a844"/>
    </svg>
    <div class="abs cocktail script">Cocktail Party<br>at Le Belvédère</div>
    <div class="abs footnote">* Program subject to change<br>** Activities in social program are optional and charged separately</div>
  </div>
</section>
<div class="page-label" style="left:441px;top:509px">PAGE 1</div>
<div class="page-label" style="left:789px;top:509px">PAGE 2</div>

<section class="spread spread--two">
  <div class="abs speakers-head">
    <div class="abs brand">Meridian Prestige Academy</div>
    <div class="abs event">Luxury Hospitality Summit®<br>Miami, Florida - 2017</div>
    <div class="abs speakers-title script">Meet our Speakers</div>
  </div>
  <div class="abs speakers-body">
    <div class="abs speakers-intro">
      <p>There are many variations of passages of Lorem Ipsum available, but the majority have suffered alteration in some form, by injected humour, or randomised words which don't look even slightly believable.</p>
      <p>If you are going to use a passage of Lorem Ipsum, you need to be sure there isn't anything embarrassing hidden in the middle of text.</p>
    </div>
    <div class="speaker" style="left:129px">
      <div class="speaker-photo" role="img" aria-label="Portrait of keynote speaker"></div>
      <div class="speaker-name">Laurent Devaux</div>
      <div class="speaker-role">Executive Vice President<br>of Maison Verlaine Group<br>between 1996 and 2009</div>
      <div class="speaker-bio">There are many variations of passages of Lorem Ipsum available, but the majority have suffered alteration in some form, by injected humour, or randomised words which don't look even slightly believable.</div>
    </div>
    <div class="speaker" style="left:212px">
      <div class="speaker-photo" role="img" aria-label="Portrait of keynote speaker"></div>
      <div class="speaker-name">Laurent Devaux</div>
      <div class="speaker-role">Executive Vice President<br>of Maison Verlaine Group<br>between 1996 and 2009</div>
      <div class="speaker-bio">There are many variations of passages of Lorem Ipsum available, but the majority have suffered alteration in some form, by injected humour, or randomised words which don't look even slightly believable.</div>
    </div>
    <div class="speaker" style="left:296px">
      <div class="speaker-photo" role="img" aria-label="Portrait of keynote speaker"></div>
      <div class="speaker-name">Laurent Devaux</div>
      <div class="speaker-role">Executive Vice President<br>of Maison Verlaine Group<br>between 1996 and 2009</div>
      <div class="speaker-bio">There are many variations of passages of Lorem Ipsum available, but the majority have suffered alteration in some form, by injected humour, or randomised words which don't look even slightly believable.</div>
    </div>
  </div>

  <div class="abs topics-col">
    <div class="topics-title script">Content Topics</div>
    <ul>
      <li>There are many variations of pas sages of Lorem Ipsum available, but the</li>
      <li>There are many variations of pas sages of Lorem Ipsum available, but the</li>
      <li>There are many variations of pas sages of Lorem Ipsum available, but the</li>
      <li>There are many variations of pas sages of Lorem Ipsum available, but the</li>
      <li>There are many variations of pas sages of Lorem Ipsum available, but the</li>
      <li>There are many variations of pas sages of Lorem Ipsum available, but the</li>
      <li>There are many variations of pas sages of Lorem Ipsum available, but the</li>
      <li>There are many variations of pas sages of Lorem Ipsum available, but the</li>
      <li>There are many variations of pas sages of Lorem Ipsum available, but the</li>
    </ul>
  </div>
  <div class="abs pool-photo" role="img" aria-label="Resort pool with palm trees and a white cabana"></div>
  <div class="abs highlights">
    <div class="highlights-title script">Course highlights</div>
    <p>There are many variations of pas sages of Lorem Ipsum available, but the</p>
    <p>There are many variations of pas sages of Lorem Ipsum available, but the</p>
  </div>
</section>
<div class="page-label" style="left:410px;top:1085px">PAGE 3</div>
<div class="page-label" style="left:736px;top:1085px">PAGE 4</div>

</body>
</html>
```